Corvelle Strategies business card

I need a business card for my new strategic consulting LLC, Corvelle Strategies. We specialize in helping people who care about broadband technology and telecommunications policy, and we're based in Washington DC. I'm looking for a card that says smart, credible, future-facing and signals a high level of expertise. It's DC, so there's clearly a limit to how crazy we can go with this card, but I am looking for a design that reflects a company that is comfortable with technology, policy, and having a little bit fun. I'm uploading my logo below, and I'd like to have it be part of the card design in some fashion.
Target Market(s)
Telecommunications and technology policy professionals
Industry/Entity Type
Technology policy
Contact Information for Business Card
Name of business, my name (Glen Mosswater), email (glen@corvellestrategies-example.com) , phone number (202-555-0148)phone number

```html
<!DOCTYPE html>
<html lang="en">
<head>
<meta charset="utf-8">
<title>Corvelle Strategies – Business Card</title>
<link rel="stylesheet" href="https://fonts.googleapis.com/css2?family=Montserrat:wght@500;600;700;800&display=swap">
<style>
  :root {
    --brand-blue: #0b56a8;
    --brand-orange: #f4ad3d;
    --paper: #f7f6f2;
    --stage: #3a3a3a;
    --white: #ffffff;
  }
  * { box-sizing: border-box; margin: 0; padding: 0; }
  html, body {
    width: 1200px; height: 689px; overflow: hidden;
    background: var(--stage);
    font-family: "Montserrat", Arial, sans-serif;
  }
  .canvas {
    position: relative; width: 1200px; height: 689px;
    display: flex; align-items: center; justify-content: center; gap: 60px;
  }
  .card {
    position: relative; width: 520px; height: 298px; overflow: hidden;
    border-radius: 3px;
  }

  /* Front */
  .card-front { background: var(--paper); }
  .front-band { position: absolute; inset: 0; }
  .front-art {
    position: absolute; right: 20px; top: 14px; width: 150px; height: 90px;
    background: linear-gradient(160deg, #f4ad3d 0%, #f4ad3d 20%, #1a63b4 21%, #0b56a8 100%);
    border-radius: 4px;
  }
  .wordmark {
    position: absolute; left: 30px; top: 44px;
    display: flex; align-items: center; gap: 9px;
    font-weight: 800; font-size: 26px; letter-spacing: -.4px; line-height: 1;
    color: var(--brand-blue);
    white-space: nowrap;
  }
  .wordmark-dot {
    width: 14px; height: 14px; border-radius: 50%;
    background: var(--brand-orange); flex: none;
  }
  .person-name {
    position: absolute; left: 30px; top: 108px;
    font-weight: 600; font-size: 22px; line-height: 1.2; color: var(--brand-blue);
  }
  .person-name .surname { color: var(--brand-orange); }
  .contact-list {
    position: absolute; left: 30px; bottom: 20px; list-style: none;
    font-weight: 500; font-size: 13px; color: var(--brand-blue);
  }
  .contact-list li { display: flex; align-items: center; gap: 8px; line-height: 1.7; }
  .contact-list svg { width: 13px; height: 13px; flex: none; }

  /* Back */
  .card-back {
    background: var(--brand-blue);
    display: flex; align-items: center; justify-content: center;
  }
  .back-pattern {
    position: absolute; inset: 0;
    background: linear-gradient(135deg, #0c5cb4 0%, #0a52a2 50%, #0c5cb4 100%);
  }
  .card-back .wordmark {
    position: relative; left: auto; top: auto;
    color: var(--white); font-size: 34px;
  }
  .card-back .wordmark-dot { width: 16px; height: 16px; }
</style>
</head>
<body>
<main class="canvas">

  <section class="card card-front" aria-label="Card front">
    <svg class="front-band" viewBox="0 0 520 298" preserveAspectRatio="none" aria-hidden="true">
      <path d="M0 298 L0 226 C160 194 340 114 520 74 L520 298 Z" fill="var(--brand-orange)"/>
      <path d="M0 222 C160 190 340 110 520 70" fill="none" stroke="var(--brand-blue)" stroke-width="5"/>
    </svg>
    <div class="front-art" role="img" aria-label="Illustration of blue mountains with a rising orange sun and a winding river"></div>

    <div class="wordmark"><span class="wordmark-dot"></span>Corvelle Strategies</div>

    <p class="person-name">Glen <span class="surname">Mosswater</span></p>

    <ul class="contact-list">
      <li>
        <svg viewBox="0 0 24 24" fill="var(--brand-blue)" aria-hidden="true"><path d="M6.6 10.8a15 15 0 0 0 6.6 6.6l2.2-2.2a1 1 0 0 1 1-.25 11.4 11.4 0 0 0 3.6.57 1 1 0 0 1 1 1V20a1 1 0 0 1-1 1A17 17 0 0 1 3 4a1 1 0 0 1 1-1h3.5a1 1 0 0 1 1 1c0 1.25.2 2.45.57 3.57a1 1 0 0 1-.25 1z"/></svg>
        202-555-0148
      </li>
      <li>
        <svg viewBox="0 0 24 24" fill="none" stroke="var(--brand-blue)" stroke-width="2" aria-hidden="true"><rect x="3" y="5" width="18" height="14" rx="2"/><path d="M3 7l9 6 9-6"/></svg>
        glen@corvellestrategies-example.com
      </li>
    </ul>
  </section>

  <section class="card card-back" aria-label="Card back">
    <div class="back-pattern" role="img" aria-label="Subtle embossed repeating pattern of the brand mark"></div>
    <div class="wordmark"><span class="wordmark-dot"></span>Corvelle Strategies</div>
  </section>

</main>
</body>
</html>
```